Business Card Design Project

I want a cleaner business card and envelope then what we have now, its too crowded.
Updates

I update with logo, this can be changed anyway you feel it looks best. I also have put gaurantee on there and extended time, this is my first time doing this. Also gave an example of current card

Target Market(s)

a wide array of customers from lattice 700 to small companies and cleints

Industry/Entity Type

Business

Requirements
Must have
• Need to have address, telephone number email
Nice to have
• a sharp professional card that stands out but is still very clean.
Should not have
• Not crazy looking

```html
<!DOCTYPE html>
<html lang="en">
<head>
<meta charset="utf-8">
<title>Harborpoint Insurance Group – Stationery</title>
<link href="https://fonts.googleapis.com/css2?family=Source+Sans+3:wght@400;600&display=swap" rel="stylesheet">
<style>
  :root {
    --bg-top: #2a2a2a;
    --bg-mid: #7a7a7c;
    --bg-bottom: #d6d6d8;
    --navy: #1a4277;
    --navy-deep: #173a6c;
    --blue-bright: #1a6fba;
    --white: #ffffff;
    --black: #000000;
    --silver: #a9abae;
    --steel: #8a8c90;
    --rule: #c9cdd3;
    --card-edge: #bfc1c4;
    --ink-dark: #2d2f33;
    --text-font: "Source Sans 3", "Myriad Pro", Arial, sans-serif;
  }
  * { box-sizing: border-box; margin: 0; padding: 0; }
  html, body { width: 1200px; height: 1200px; overflow: hidden; }
  body {
    position: relative;
    font-family: var(--text-font);
    background: linear-gradient(180deg, var(--bg-top) 0%, var(--bg-mid) 40%, var(--bg-bottom) 100%);
  }

  /* ---------- Brand name (replaces mark) ---------- */
  .brand { display: flex; align-items: center; gap: 16px; }
  .brand-square { flex: none; background: var(--steel); }
  .brand-name { font-weight: 600; letter-spacing: 0.06em; line-height: 1.05; text-transform: uppercase; }

  /* ---------- Front of card ---------- */
  .card {
    position: absolute;
    left: 362px; width: 512px; height: 307px;
    border: 2px solid var(--card-edge);
    overflow: hidden;
  }
  .card-front { top: 53px; background: var(--white); }
  .card-front .brand { position: absolute; left: 78px; top: 26px; }
  .card-front .brand-square { width: 104px; height: 104px; }
  .card-front .brand-name { color: var(--ink-dark); font-size: 26px; }

  .front-band {
    position: absolute; left: 0; right: 0; top: 153px; bottom: 0;
    background: linear-gradient(160deg, var(--navy-deep) 0%, var(--navy) 65%, var(--blue-bright) 100%);
  }
  .front-rule { position: absolute; left: 0; top: 16px; width: 446px; height: 2px; background: var(--rule); }
  .person { position: absolute; right: 296px; top: 40px; text-align: right; color: var(--white); }
  .person-name { font-size: 23px; font-weight: 600; white-space: nowrap; }
  .person-title { font-size: 17px; font-weight: 400; margin-top: 6px; }
  .band-divider {
    position: absolute; left: 241px; top: 40px; width: 1px; height: 94px;
    background: linear-gradient(180deg, transparent, var(--rule) 20%, var(--rule) 80%, transparent);
  }
  .contact-list { position: absolute; left: 254px; top: 50px; list-style: none; color: var(--white); font-size: 13px; }
  .contact-list li { display: flex; align-items: center; gap: 8px; height: 25px; white-space: nowrap; }
  .contact-list svg { width: 16px; height: 14px; flex: none; }

  /* ---------- Back of card ---------- */
  .card-back { top: 427px; background: var(--black); }
  .tab {
    position: absolute; background: var(--silver); color: var(--white);
    text-align: center; font-size: 12px;
  }
  .tab-address { left: 180px; top: 0; width: 175px; height: 36px; border-radius: 0 0 10px 10px; line-height: 14px; padding-top: 4px; }
  .tab-web { left: 120px; bottom: 0; width: 295px; height: 22px; border-radius: 10px 10px 0 0; line-height: 23px; font-size: 15px; letter-spacing: 0.04em; }
  .card-back .brand { position: absolute; left: 58px; top: 100px; }
  .card-back .brand-square { width: 100px; height: 100px; }
  .card-back .brand-name { color: var(--white); font-size: 28px; }
  .back-rule { position: absolute; left: 178px; top: 117px; right: 0; height: 2px; background: var(--rule); }

  /* ---------- Envelope ---------- */
  .envelope { position: absolute; left: 248px; top: 772px; width: 741px; height: 372px; }
  .envelope svg.flap { position: absolute; left: 0; top: 0; }
  .envelope-face { position: absolute; left: 0; right: 0; top: 184px; bottom: 0; background: var(--white); }
  .envelope .brand { position: absolute; left: 38px; top: 30px; flex-direction: column; align-items: flex-start; gap: 12px; }
  .envelope .brand-square { width: 76px; height: 76px; margin-left: 44px; }
  .envelope .brand-name { color: var(--ink-dark); font-size: 22px; }
  .return-address { position: absolute; right: 20px; bottom: 16px; text-align: right; color: var(--navy); font-size: 13px; line-height: 18px; }
</style>
</head>
<body>

<!-- Front of card -->
<section class="card card-front" aria-label="Business card front">
  <div class="brand">
    <span class="brand-square"></span>
    <span class="brand-name">Harborpoint<br>Insurance Group</span>
  </div>
  <div class="front-band">
    <span class="front-rule"></span>
    <div class="person">
      <p class="person-name">Marla Quinn-Ostrow</p>
      <p class="person-title">Operations Manager</p>
    </div>
    <span class="band-divider"></span>
    <ul class="contact-list">
      <li>
        <svg viewBox="0 0 16 14" aria-hidden="true"><rect x="5" y="1" width="6" height="12" rx="1" fill="none" stroke="#fff"/><rect x="6.5" y="3" width="3" height="3" fill="#fff"/></svg>
        555.201.4400
      </li>
      <li>
        <svg viewBox="0 0 16 14" aria-hidden="true"><rect x="1" y="2" width="14" height="10" fill="none" stroke="#fff"/><path d="M1 2l7 6 7-6M1 12l5-5M15 12l-5-5" fill="none" stroke="#fff"/></svg>
        mquinn-ostrow@harborpointagency.com
      </li>
      <li>
        <svg viewBox="0 0 16 14" aria-hidden="true"><rect x="4" y="1" width="8" height="5" fill="none" stroke="#fff"/><rect x="1" y="6" width="14" height="6" fill="#fff"/></svg>
        555.201.4403
      </li>
    </ul>
  </div>
</section>

<!-- Back of card -->
<section class="card card-back" aria-label="Business card back">
  <div class="tab tab-address">48210 Alder Crest Avenue<br>Maple Ridge, MI 48000</div>
  <span class="back-rule"></span>
  <div class="brand">
    <span class="brand-square"></span>
    <span class="brand-name">Harborpoint<br>Insurance Group</span>
  </div>
  <div class="tab tab-web">www.harborpointagency.com</div>
</section>

<!-- Envelope -->
<section class="envelope" aria-label="Envelope">
  <svg class="flap" width="741" height="184" viewBox="0 0 741 184" aria-hidden="true">
    <defs>
      <linearGradient id="envBlue" x1="0" y1="0" x2="1" y2="0">
        <stop offset="0" stop-color="#173a6c"/>
        <stop offset="0.7" stop-color="#1a4a82"/>
        <stop offset="1" stop-color="#1a6fba"/>
      </linearGradient>
    </defs>
    <path d="M0 84 L38 10 Q44 0 58 0 L680 0 Q696 0 702 10 L741 84 L741 132 L0 132 Z" fill="url(#envBlue)"/>
    <rect x="0" y="132" width="741" height="4" fill="#d3d6da"/>
    <rect x="0" y="136" width="741" height="48" fill="url(#envBlue)"/>
  </svg>
  <div class="envelope-face">
    <div class="brand">
      <span class="brand-square"></span>
      <span class="brand-name">Harborpoint<br>Insurance Group</span>
    </div>
    <p class="return-address">48210 Alder Crest Avenue<br>Maple Ridge, MI 48000</p>
  </div>
</section>

</body>
</html>
```